Social Media Post Quote #5 - Native American Organization

- KINDLE - must be included
- Protect your community. Protect Your Elders. Stay Vaccinated. must be included
- Attached, company Logo, campaign logos and sample flu social media image. - our audience likes BRIGHT colors.
- Must include image from the United States, representing Land/Nature from one of the following regions, Plains and Woodlands, or Southwest, or Mountains, or Coast.
- must include quote: Help our “early elders” achieve “older elders” status.
- One image will be provided twice - incorporating campaign logos - in some fashion
Inspiration: https://velmorhub.example/ and https://www.facebook.com/Velmorhub

```html
<!DOCTYPE html>
<html lang="en">
<head>
<meta charset="utf-8">
<title>Kindle – Stay Vaccinated</title>
<link rel="stylesheet" href="https://fonts.googleapis.com/css2?family=Montserrat:wght@700&family=Poppins:wght@400;500;700&family=Roboto+Condensed:wght@700&display=swap">
<style>
  :root {
    --page-bg: #ededed;
    --frame-teal: #5fa3a5;
    --frame-rust: #b7685c;
    --sky-deep: #0b3f93;
    --sky-mid: #1b78cc;
    --sky-haze: #cfe1ef;
    --rock-light: #b4622f;
    --rock-mid: #7e3520;
    --rock-dark: #3e1710;
    --teal: #4fa3a3;
    --white: #ffffff;
    --vaccine-red: #6a2620;
  }
  * { margin: 0; padding: 0; box-sizing: border-box; }
  html, body {
    width: 1112px; height: 1200px; overflow: hidden;
    background: var(--page-bg);
  }
  .post {
    position: absolute; left: 156px; top: 200px;
    width: 800px; height: 800px;
  }
  .post-frame {
    position: absolute; inset: 0;
    background: linear-gradient(135deg, var(--frame-teal), var(--frame-rust) 50%, var(--frame-teal));
  }
  .post-landscape {
    position: absolute; left: 30px; top: 30px; right: 30px; bottom: 30px;
    background: linear-gradient(180deg,
      var(--sky-deep) 0%,
      var(--sky-mid) 38%,
      var(--sky-haze) 52%,
      var(--rock-light) 60%,
      var(--rock-mid) 78%,
      var(--rock-dark) 100%);
  }
  .headline-box {
    position: absolute; left: 61px; top: 79px;
    width: 459px; height: 106px;
    border: 3px solid var(--teal);
    display: flex; align-items: center; justify-content: center;
  }
  .headline {
    font-family: "Montserrat", sans-serif; font-weight: 700;
    font-size: 68px; letter-spacing: 1px; color: var(--white);
  }
  .brand {
    position: absolute; left: 567px; top: 100px; width: 144px;
    display: flex; align-items: center; gap: 8px;
    font-family: "Poppins", sans-serif; font-weight: 700;
    font-size: 22px; color: var(--teal);
  }
  .brand-dot { width: 14px; height: 14px; border-radius: 50%; background: var(--teal); flex: none; }
  .protect {
    position: absolute; left: 63px; top: 225px;
    font-family: "Poppins", sans-serif; font-weight: 500;
    font-size: 45px; line-height: 45px; color: var(--white);
  }
  .protect strong { font-weight: 700; }
  .stay {
    position: absolute; left: 67px; top: 310px;
    font-family: "Roboto Condensed", sans-serif; font-weight: 700;
    font-size: 82px; line-height: 82px; color: var(--vaccine-red);
  }
  .quote {
    position: absolute; left: 76px; top: 646px;
    font-family: "Poppins", sans-serif; font-weight: 400;
    font-size: 33px; line-height: 39px; color: var(--white);
  }
  .quote strong { font-weight: 700; }
</style>
</head>
<body>
  <main class="post">
    <div class="post-frame" role="img" aria-label="Woven chevron border pattern in teal and rust"></div>
    <div class="post-landscape" role="img" aria-label="Southwest canyon landscape with red sandstone, a lake and a bright blue sky"></div>

    <div class="headline-box"><h1 class="headline">KINDLE</h1></div>

    <div class="brand"><span class="brand-dot"></span>Velmorhub</div>

    <p class="protect">PROTECT YOUR <strong>COMMUNITY</strong><br>PROTECT YOUR <strong>ELDERS</strong></p>
    <p class="stay">STAY VACCINATED</p>

    <p class="quote">HELP OUR <strong>“EARLY ELDERS”</strong><br>ACHIEVE <strong>“OLDER ELDERS”</strong> STATUS</p>
  </main>
</body>
</html>
```